Water Filter Company Needs Bizz Cards!!

Need business cards for my company. We sell whole home water filters and salt free water softeners. No more buying bottled water. Our filtering units filter out all heavy metals, chlorine, and VOC's, last 15 years, and are maintenance free and supply your whole home with spring quality alkaline water. Our Salt free water conditioners, eliminate hard water and scale, without lowering the ph, or TDS's (total Dissolved solids)

I think this is the color code we are using on my site. My logo looks good behind it. #192841

Website will be www.Brovexa.com

Industry/Entity Type

Water Purification

Contact Information for Business Card

For now, just insert standard Dummy text. I need these text lines for the info to be editable so i can make them for multiple employees. I do have Photoshop and illustrator, unless there is a simpler program i can use solely for biz cards

Font styles to use
Sans Serif

Requirements
Must have
• Use my preexisting logo.

www.BroVexa.com

Spring Quality Alkaline Water at every tap.

List out services. Whole Home Water Filters, Salt Free Water Softeners, Clarimont KT7, UV Sterilizers
Nice to have
• I think this is the color code we are using on my site. My logo looks good behind it. #192841 or black. Please no white or light blue backgrounds.

Maybe a picture of my tank.

Slogan like Spring Quality Alkaline Water at every tap.
And just list the services Whole Home Water Filters, Salt Free Water Softeners, Clarimont KT7, UV Sterilizers

I think I would like to not have a contrasting textured logo like I see on some of them. I may use it for my personal cards, but new employees may not want the extra expense.
Should not have
• A different logo than the one provided.

White or baby blue backgrounds. Use the color code, or blacks.

```html
<!DOCTYPE html>
<html lang="en">
<head>
<meta charset="utf-8">
<title>Brovexa Business Cards</title>
<link href="https://fonts.googleapis.com/css2?family=Work+Sans:wght@400;600&display=swap" rel="stylesheet">
<style>
  :root {
    --stage: #1e1e1f;
    --card-dark: #141414;
    --card-navy: #192841;
    --brand-blue: #1591d6;
    --brand-sky: #45bdea;
    --ink-light: #e6ecf3;
    --ink-soft: #aebbd0;
  }
  html, body {
    margin: 0;
    width: 1200px;
    height: 930px;
    overflow: hidden;
    background: var(--stage);
    font-family: "Work Sans", sans-serif;
  }
  .stage { position: relative; width: 1200px; height: 930px; }
  .card {
    position: absolute;
    width: 540px;
    height: 309px;
    border-radius: 16px;
    overflow: hidden;
    box-shadow: 0 18px 40px rgba(0,0,0,.55);
  }
  .card--back { left: 90px; top: 150px; background: var(--card-dark); }
  .card--front { left: 570px; top: 470px; background: var(--card-navy); }

  .brand {
    position: absolute;
    display: flex;
    align-items: center;
    gap: 12px;
  }
  .brand__dot {
    width: 30px; height: 30px; border-radius: 50%;
    background: var(--brand-sky);
  }
  .brand__name {
    font-weight: 600;
    font-size: 52px;
    letter-spacing: -1px;
    color: var(--brand-sky);
    line-height: 1;
  }
  .card--back .brand { left: 112px; top: 122px; }
  .card--front .brand { left: 32px; top: 58px; }
  .card--front .brand__name { font-size: 42px; }
  .card--front .brand__dot { width: 24px; height: 24px; }

  .slogan {
    position: absolute;
    left: 32px; top: 112px;
    margin: 0;
    width: 260px;
    font-size: 12px;
    color: var(--ink-light);
  }
  .services {
    position: absolute;
    left: 32px; top: 142px;
    margin: 0; padding: 0;
    list-style: none;
    display: grid;
    grid-template-columns: 142px 130px;
    row-gap: 6px;
    font-size: 10.5px;
    color: var(--ink-soft);
  }
  .services li { display: flex; align-items: center; gap: 6px; }
  .services li::before {
    content: "";
    width: 5px; height: 5px; border-radius: 50%;
    background: var(--brand-sky);
    flex: none;
  }

  .divider {
    position: absolute;
    left: 300px; top: 44px;
    width: 1px; height: 160px;
    background: var(--brand-blue);
  }
  .contact {
    position: absolute;
    left: 320px; top: 38px;
    color: var(--ink-light);
    font-size: 13px;
    line-height: 1.5;
  }
  .contact__name {
    margin: 0;
    color: var(--brand-sky);
    font-weight: 600;
    font-size: 18px;
    letter-spacing: .3px;
  }
  .contact__role { margin: 0 0 6px; font-size: 13.5px; color: var(--ink-soft); }
  .contact__address { margin: 0 0 4px; }
  .contact__list { list-style: none; margin: 0; padding: 0; }
  .contact__list li { display: flex; align-items: center; gap: 7px; }
  .contact__list svg { width: 11px; height: 11px; fill: none; stroke: var(--brand-sky); stroke-width: 1.6; }

  .band { position: absolute; left: 0; bottom: 0; width: 540px; height: 80px; }
</style>
</head>
<body>
<main class="stage">
  <section class="card card--back" aria-label="Card back">
    <div class="brand">
      <span class="brand__dot"></span>
      <span class="brand__name">Brovexa</span>
    </div>
  </section>

  <section class="card card--front" aria-label="Card front">
    <div class="brand">
      <span class="brand__dot"></span>
      <span class="brand__name">Brovexa</span>
    </div>
    <p class="slogan">Spring Quality Alkaline Water at every tap.</p>
    <ul class="services">
      <li>Whole Home Water Filters</li>
      <li>Salt Free Water Softeners</li>
      <li>Clarimont KT7</li>
      <li>UV Sterilizers</li>
    </ul>
    <div class="divider"></div>
    <div class="contact">
      <h1 class="contact__name">DANIEL HART</h1>
      <p class="contact__role">Founder</p>
      <p class="contact__address">48 Linden Park Road,<br>Westbrook, OR</p>
      <ul class="contact__list">
        <li><svg viewBox="0 0 12 12"><path d="M2 1.5l2 .2.8 2.3-1.2 1a6 6 0 0 0 3.4 3.4l1-1.2 2.3.8.2 2A1 1 0 0 1 9.5 11 8.5 8.5 0 0 1 1 2.5a1 1 0 0 1 1-1z"/></svg>1 503 555 0142</li>
        <li><svg viewBox="0 0 12 12"><rect x="1" y="2.5" width="10" height="7" rx="1"/><path d="M1 3l5 3.5L11 3"/></svg>info@Brovexa.com</li>
        <li><svg viewBox="0 0 12 12"><circle cx="6" cy="6" r="5"/><path d="M1 6h10M6 1c2.5 2.7 2.5 7.3 0 10M6 1c-2.5 2.7-2.5 7.3 0 10"/></svg>www.BroVexa.com</li>
      </ul>
    </div>
    <svg class="band" viewBox="0 0 540 80" preserveAspectRatio="none" aria-hidden="true">
      <polygon points="0,56 540,56 540,80 0,80" fill="#45bdea"/>
      <polygon points="340,56 540,0 540,80 340,80" fill="#1591d6"/>
      <circle cx="340" cy="56" r="9" fill="#192841"/>
    </svg>
  </section>
</main>
</body>
</html>
```